Business Card for my Photography/Video Business

I would like the card to say Event Photographer and Videographer. I like the Black and Gold look to it as well but open to other options. I don't want it to be super vibrant or colorful. Simple, elegant and professional

```html
<!DOCTYPE html>
<html lang="en">
<head>
<meta charset="utf-8">
<title>Vespera – Business Card</title>
<link href="https://fonts.googleapis.com/css2?family=Lato:wght@400;700&display=swap" rel="stylesheet">
<style>
  :root {
    --backdrop: #7b7b7b;
    --card: #0f0f0f;
    --gold: #d1ad3c;
    --gold-muted: #b8962f;
    --text-grey: #a6a6a6;
    --rule: #6d6d6d;
  }
  html, body {
    margin: 0;
    padding: 0;
    overflow: hidden;
  }
  .canvas {
    position: relative;
    width: 1200px;
    height: 1200px;
    background: var(--backdrop);
    font-family: "Lato", sans-serif;
    overflow: hidden;
  }
  .card {
    position: absolute;
    top: 310px;
    height: 594px;
    background: var(--card);
  }
  .card--front { left: 234px; width: 364px; }
  .card--back  { left: 627px; width: 370px; }

  .brand {
    position: absolute;
    display: flex;
    align-items: center;
    gap: 12px;
  }
  .brand__dot {
    width: 82px;
    height: 82px;
    border-radius: 50%;
    background: var(--gold);
    flex: none;
  }
  .brand__name {
    font-weight: 700;
    font-size: 44px;
    letter-spacing: 2px;
    color: var(--gold);
    line-height: 1;
  }
  .card--front .brand { left: 33px; top: 161px; }
  .card--back .brand  { left: 36px; top: 257px; }

  .person {
    position: absolute;
    left: 0;
    right: 0;
    top: 368px;
    text-align: center;
  }
  .person__name {
    font-weight: 700;
    font-size: 21px;
    color: var(--gold);
    line-height: 1;
  }
  .person__role {
    font-size: 16.5px;
    color: var(--text-grey);
    margin-top: 3px;
    white-space: nowrap;
  }

  .contact-icons {
    position: absolute;
    left: 87px;
    top: 448px;
    width: 190px;
    height: 24px;
  }

  .contact-list {
    position: absolute;
    left: 0;
    right: 0;
    top: 484px;
    margin: 0;
    padding: 0;
    list-style: none;
    text-align: center;
    font-size: 16.5px;
    line-height: 22px;
    color: var(--text-grey);
  }

  .web-address {
    position: absolute;
    left: 0;
    right: 0;
    top: 535px;
    text-align: center;
    font-size: 15px;
    letter-spacing: 3px;
    color: var(--gold);
  }
</style>
</head>
<body>
<main class="canvas">

  <section class="card card--front" aria-label="Card front">
    <div class="brand">
      <span class="brand__dot"></span>
      <span class="brand__name">VESPERA</span>
    </div>

    <div class="person">
      <div class="person__name">MARCUS HALE</div>
      <div class="person__role">Event Photographer and Videographer</div>
    </div>

    <svg class="contact-icons" viewBox="0 0 190 24" aria-hidden="true">
      <line x1="0" y1="12" x2="52" y2="12" stroke="var(--rule)" stroke-width="1"/>
      <line x1="138" y1="12" x2="190" y2="12" stroke="var(--rule)" stroke-width="1"/>
      <circle cx="67" cy="12" r="12" fill="var(--gold)"/>
      <path d="M61 9 q6 -5 12 0 l-1.5 2 h-2 v-1.5 h-5 v1.5 h-2 z M62 16 l2 -4 h6 l2 4 z" fill="var(--card)"/>
      <circle cx="95" cy="12" r="12" fill="var(--gold)"/>
      <rect x="88.5" y="7.5" width="13" height="9" fill="none" stroke="var(--card)" stroke-width="1.6"/>
      <path d="M88.5 7.5 L95 13 L101.5 7.5" fill="none" stroke="var(--card)" stroke-width="1.6"/>
      <circle cx="123" cy="12" r="12" fill="var(--gold)"/>
      <circle cx="123" cy="12" r="6.5" fill="none" stroke="var(--card)" stroke-width="1.5"/>
      <ellipse cx="123" cy="12" rx="2.8" ry="6.5" fill="none" stroke="var(--card)" stroke-width="1.2"/>
      <line x1="116.5" y1="12" x2="129.5" y2="12" stroke="var(--card)" stroke-width="1.2"/>
    </svg>

    <ul class="contact-list">
      <li>055-987 654 321</li>
      <li>hello@vespera.com</li>
      <li>www.vespera.com</li>
    </ul>
  </section>

  <section class="card card--back" aria-label="Card back">
    <div class="brand">
      <span class="brand__dot"></span>
      <span class="brand__name">VESPERA</span>
    </div>
    <div class="web-address">WWW.VESPERA.COM</div>
  </section>

</main>
</body>
</html>
```